Brisk Hive 360 Postcard Design, Double-Sided

Please read carefully and see attached. Designers that do not follow these instructions will not be selected. Limit ONE design submission per artist. The ONE design submission shall show both the front and the back designs. Designs must comply with the attached dismensions accounting for the bleed area to prevent designs from being cut off during printing. The attached business card and door tag designs have already been created, printed and are in use. The postcard shall be similar in design to the attached business card and door tag. All of the information that you need is attached. The overall size is 4.12" x 6.12" for the front. The back is different, see attached and scale to match template. I would like the Veteran Owned Business logo added as well. It would also be nice to see my photo incorporated somehow. I like the yellow on the door tag. It helps build contrast and pops out. Again, one design submission per designer that shows both the front and the back.

Target Market(s)

Please read all instructions and see attached.

Industry/Entity Type

Requirements
Must have
• Please read all instructions and see attached.
Nice to have
Should not have

```html
<!DOCTYPE html>
<html lang="en">
<head>
<meta charset="utf-8">
<title>Brisk Hive 360 Handyman Postcard</title>
<link href="https://fonts.googleapis.com/css2?family=Poppins:ital,wght@0,400;0,500;0,600;0,700;0,800;1,800&display=swap" rel="stylesheet">
<style>
  :root{
    --stage:#7d7d7d;
    --ink:#0b0b0b;
    --yellow:#f6a91b;
    --orange:#e9892a;
    --gold-line:#7a5a1c;
    --white:#ffffff;
    --red:#d8291c;
    --photo-grey:#9aa0a6;
  }
  *{margin:0;padding:0;box-sizing:border-box}
  html,body{width:901px;height:1200px;overflow:hidden;background:var(--stage);font-family:'Poppins',sans-serif;color:var(--white)}
  .card{position:absolute;left:76px;width:749px;height:514px;background:var(--ink);overflow:hidden}
  .card--front{top:40px}
  .card--back{top:626px}
  .abs{position:absolute}

  /* front */
  .brand-title{left:0;right:0;top:30px;text-align:center;color:var(--yellow);font-weight:800;font-style:italic;font-size:25px;line-height:30px;letter-spacing:.5px}
  .brand-title span{display:inline-block;border-bottom:2px solid var(--yellow);padding:0 2px}
  .header-rule{left:0;right:0;top:98px;height:2px;background:var(--gold-line)}
  .badge{left:35px;top:27px;width:72px;height:72px;border-radius:50%;background:#2b3d8f;border:4px solid var(--red)}
  .brand-mark{left:640px;top:48px;width:90px;text-align:center;font-weight:600;font-size:12px;line-height:15px;color:var(--white)}
  .service{width:70px;height:70px;border-radius:50%;border:3px solid var(--yellow);overflow:hidden}
  .service svg{display:block;width:100%;height:100%}
  .service-label{font-weight:600;font-size:15.5px;white-space:nowrap;transform:translateX(-50%)}
  .footer-band{left:0;right:0;top:431px;height:83px;background:linear-gradient(90deg,var(--yellow),var(--orange))}
  .owner-role{left:33px;top:445px;color:var(--ink);font-size:16px;line-height:19px}
  .owner-name{left:33px;top:462px;color:var(--ink);font-weight:700;font-size:20px;line-height:26px;border-bottom:2px solid var(--ink);white-space:nowrap}
  .inquire{left:574px;top:445px;color:var(--ink);font-size:15px;line-height:18px}
  .phone-number{left:558px;top:461px;color:var(--red);font-weight:700;font-size:21px;line-height:28px;letter-spacing:-.2px;border-bottom:1.5px solid var(--red);white-space:nowrap}
  .phone-icon{left:530px;top:463px}
  .portrait{left:242px;top:222px}

  /* back */
  .top-strip{left:0;top:0}
  .about-title{left:33px;top:36px;font-size:18px;font-weight:500}
  .about-text{left:33px;top:70px;width:402px;font-size:14.2px;line-height:17.6px}
  .thumb{width:152px;height:78px}
  .benefits-title{left:33px;top:352px;color:var(--yellow);font-weight:700;font-size:23px;letter-spacing:.5px}
  .benefit{font-size:15.5px;line-height:20px;padding-left:17px;position:absolute;white-space:nowrap}
  .benefit::before{content:"";position:absolute;left:0;top:7px;width:8px;height:8px;border-radius:50%;background:var(--white)}
  .stamp-box{left:605px;top:34px;width:111px;height:110px;background:var(--white)}
  .address-box{left:375px;top:258px;width:341px;height:171px;background:var(--white)}
  .address-row{height:33px;border-bottom:1px solid #9a9a9a;color:#111;font-size:15.5px;line-height:33px;padding-left:13px}
  .address-row:last-child{border-bottom:none}
</style>
</head>
<body>

<section class="card card--front" aria-label="Postcard front">
  <div class="abs badge" role="img" aria-label="Veteran owned business badge"></div>
  <h1 class="abs brand-title"><span>BRISK HIVE 360</span><br><span>HANDYMAN</span></h1>
  <div class="abs brand-mark">Brisk Hive 360</div>
  <div class="abs header-rule"></div>

  <svg class="abs" width="749" height="431" style="left:0;top:0" aria-hidden="true">
    <g fill="none" stroke="#fff" stroke-width="1.6" stroke-dasharray="6 5">
      <path d="M290 216 Q320 240 345 250"/>
      <path d="M296 306 Q300 330 310 345"/>
      <path d="M445 306 Q440 330 435 345"/>
      <path d="M185 370 Q220 340 280 360"/>
      <path d="M465 360 Q520 340 565 350"/>
    </g>
    <g fill="#0b0b0b" stroke="#fff" stroke-width="1.5">
      <circle cx="288" cy="216" r="3.5"/>
      <circle cx="295" cy="318" r="3.5"/>
      <circle cx="446" cy="318" r="3.5"/>
      <circle cx="170" cy="382" r="3.5"/>
      <circle cx="568" cy="380" r="3.5"/>
    </g>
  </svg>

  <div class="abs service" style="left:340px;top:115px" role="img" aria-label="Photo of a wireless video doorbell">
    <svg><rect width="70" height="70" fill="#6c6f72"/></svg>
  </div>
  <div class="abs service-label" style="left:375px;top:187px">Wireless Device Setup</div>

  <div class="abs service" style="left:210px;top:219px" role="img" aria-label="Photo of a cracked wall patch">
    <svg><rect width="70" height="70" fill="#b7bcbd"/></svg>
  </div>
  <div class="abs service-label" style="left:245px;top:293px">Small Repair</div>

  <div class="abs service" style="left:470px;top:219px" role="img" aria-label="Photo of hands fixing a pipe">
    <svg><rect width="70" height="70" fill="#8a7f78"/></svg>
  </div>
  <div class="abs service-label" style="left:505px;top:293px">Small Repairs</div>

  <div class="abs service" style="left:87px;top:306px" role="img" aria-label="Photo of furniture assembly parts">
    <svg><rect width="70" height="70" fill="#9e9588"/></svg>
  </div>
  <div class="abs service-label" style="left:122px;top:382px">Assembly</div>

  <div class="abs service" style="left:588px;top:306px" role="img" aria-label="Photo of picture hanging hardware">
    <svg><rect width="70" height="70" fill="#c9c3b6"/></svg>
  </div>
  <div class="abs service-label" style="left:623px;top:382px">Item Hanging</div>

  <div class="abs footer-band"></div>
  <div class="abs owner-role">OWNER &amp; HANDYMAN</div>
  <div class="abs owner-name">DARREN K. HOLTZ</div>

  <svg class="abs portrait" width="270" height="292" role="img" aria-label="Photo of the owner in a grey polo shirt">
    <path d="M95 0 H175 Q185 0 185 10 V120 Q250 140 268 170 L275 292 H-5 L2 180 Q20 140 85 120 V10 Q85 0 95 0Z" fill="#fff"/>
    <path d="M98 4 H172 Q181 4 181 13 V124 Q244 144 263 173 L270 292 H0 L7 183 Q25 145 89 124 V13 Q89 4 98 4Z" fill="var(--photo-grey)"/>
  </svg>

  <svg class="abs phone-icon" width="26" height="36" viewBox="0 0 26 36" aria-hidden="true">
    <rect x="2" y="2" width="18" height="32" rx="3" fill="none" stroke="var(--red)" stroke-width="2.5"/>
    <path d="M10 12 q-3 2 0 9 q3 5 7 4 l1-3 -3-2 -2 1 q-2-2-3-5 l2-1 -1-3z" fill="var(--red)"/>
  </svg>
  <div class="abs inquire">TEXT TO INQUIRE</div>
  <div class="abs phone-number">(555) 014-3820</div>
</section>

<section class="card card--back" aria-label="Postcard back">
  <svg class="abs top-strip" width="749" height="22" aria-hidden="true">
    <path d="M0 0 H749 V14 Q375 22 0 18Z" fill="var(--yellow)"/>
  </svg>
  <h2 class="abs about-title">About us</h2>
  <p class="abs about-text">Lorem ipsum dolor sit amet, consectetur adipiscing elit, sed do eiusmod tempor incididunt ut labore et dolore magna aliqua. Quis ipsum suspendisse ultrices gravida. Risus commodo viverra maecenas ac-</p>

  <div class="abs thumb" style="left:33px;top:166px;background:linear-gradient(135deg,#d9d9d9,#4a4a4a)" role="img" aria-label="Photo of a cabinet being assembled"></div>
  <div class="abs thumb" style="left:206px;top:166px;background:radial-gradient(circle at 50% 50%,#3fa3e0,#0c2d5e)" role="img" aria-label="Illustration of connected home wireless devices"></div>
  <div class="abs thumb" style="left:33px;top:258px;background:linear-gradient(135deg,#8a6a3e,#2b5f6b)" role="img" aria-label="Photo of a tool belt with hand tools"></div>
  <div class="abs thumb" style="left:206px;top:258px;background:linear-gradient(135deg,#2a2a2a,#8c2b2e)" role="img" aria-label="Photo of holiday lights on a ladder"></div>

  <h3 class="abs benefits-title">BENEFITS</h3>
  <div class="benefit" style="left:33px;top:389px">Fast Response</div>
  <div class="benefit" style="left:177px;top:389px">Fair Pricing</div>
  <div class="benefit" style="left:33px;top:413px">High Quality</div>
  <div class="benefit" style="left:177px;top:413px">Veteran Owned</div>

  <div class="abs stamp-box"></div>
  <div class="abs address-box">
    <div class="address-row">Jhon Smith</div>
    <div class="address-row">123 main street</div>
    <div class="address-row">small town, USA 000 000 000</div>
    <div class="address-row"></div>
    <div class="address-row"></div>
  </div>
</section>

</body>
</html>
```